58 Restaurant & Bar Menu

Want to make current menu more trendy in design. I have attached a pdf of the menu and of the logo. Rather, than being 6 pages I would like to make the menu into "4 pages". The menu will be printed in color.

I am open to designs that will allow the menu to be printed on 11x17 paper that will be folded in half. The "Breakfast" section needs to be its own page and all the way on the back.

As for the cover I am open to just keeping it as a cover with the info I have on it but completely different design/picture change. The logo needs to stay. The cover can also be used as having menu items on there if pulled of correctly.

The readability has to be clear to the guests.

The restaurant is a Mediterranean style and for the area it is priced mid-high. The atmosphere is casual fine dining with Martini & Wine Bar. All are ingredients are fresh never frozen and everything is prepared from scratch.

Industry/Entity Type

Restaurant

Requirements
Must have
• Breakfast on its own page on the back.
Nice to have
• Trendy Design

```html
<!DOCTYPE html>
<html lang="en">
<head>
<meta charset="utf-8">
<title>58 Restaurant &amp; Bar – Breakfast Menu</title>
<link href="https://fonts.googleapis.com/css2?family=Open+Sans:wght@400;600;700&display=swap" rel="stylesheet">
<style>
:root{
  --blue:#17a6e8;
  --ink:#2f2f2f;
  --grey:#3a3a3a;
  --paper:#ffffff;
  --pattern-a:#eaf5fc;
  --pattern-b:#d3eaf8;
}
*{margin:0;padding:0;box-sizing:border-box}
html,body{width:1200px;height:777px;overflow:hidden;background:var(--paper)}
body{font-family:"Open Sans",Arial,sans-serif;color:var(--ink)}
.spread{position:relative;width:1200px;height:777px;overflow:hidden}
.damask{position:absolute;inset:0;background:radial-gradient(ellipse at 30% 30%,var(--pattern-b) 0%,var(--pattern-a) 45%,#f6fbfe 100%)}
.edge-tabs{position:absolute;left:0;top:0;width:20px;height:777px}
.page-divider{position:absolute;left:599px;top:40px;width:1px;height:696px;background:#555}

.breakfast-head{position:absolute;left:0;width:600px;top:42px;text-align:center}
.breakfast-head h1{font-size:14px;font-weight:700;color:var(--blue);line-height:17px}
.breakfast-head p{font-size:15px;font-weight:400;line-height:19px}

.section{position:absolute;font-size:8px;line-height:12.5px}
.section h2{font-size:11px;font-weight:700;line-height:16px;margin-bottom:1px}
.item{font-size:9.5px;font-weight:700;line-height:12.5px;white-space:nowrap}
.desc{font-size:8px;font-weight:400;white-space:nowrap}
.feature{color:var(--blue)}
.indent{padding-left:12px}

.cover{position:absolute;left:737px;top:0;width:321px;height:659px;background:var(--paper);border:6px solid var(--blue);border-top:none;text-align:center;color:var(--grey)}
.cover-stripe{position:absolute;left:823px;top:659px;width:146px;height:118px;background:var(--blue)}
.cover-title{position:absolute;top:133px;width:100%;font-size:29px;font-weight:700;letter-spacing:1px}
.brand{position:absolute;top:308px;left:0;width:100%;display:flex;justify-content:center;align-items:center;gap:10px}
.brand-dot{width:14px;height:14px;border-radius:50%;background:var(--blue)}
.brand-name{font-size:22px;font-weight:700;color:var(--grey)}
.contact{position:absolute;top:486px;width:100%;font-size:13px;font-weight:700;line-height:18.5px}
.cover-note{position:absolute;top:558px;width:100%;font-size:13px;font-weight:700;color:var(--blue)}
.cover-extras{position:absolute;top:593px;width:100%;font-size:13px;font-weight:700;line-height:18.5px}
</style>
</head>
<body>
<div class="spread">
  <div class="damask" role="img" aria-label="Light blue ornamental damask pattern covering the background"></div>

  <svg class="edge-tabs" viewBox="0 0 20 777" aria-hidden="true">
    <g fill="#17a6e8">
      <rect x="0" y="0" width="9" height="93"/>
      <rect x="0" y="98" width="9" height="139"/><rect x="0" y="98" width="18" height="5"/>
      <rect x="0" y="240" width="9" height="172"/><rect x="0" y="240" width="18" height="5"/>
      <rect x="0" y="425" width="9" height="120"/><rect x="0" y="425" width="18" height="5"/>
      <rect x="0" y="550" width="9" height="227"/><rect x="0" y="550" width="18" height="5"/>
    </g>
  </svg>

  <header class="breakfast-head">
    <h1>Breakfast</h1>
    <p>Served Saturday &amp; Sunday</p>
  </header>

  <section class="section" style="left:70px;top:99px">
    <h2>Skillets</h2>
    <div class="item">Veggie $6.95</div>
    <div class="desc">Skillet full of hash browns, onions, peppers, tomatoes &amp; mushrooms topped with cheese and 2 eggs. Served w/ Toast.</div>
    <div class="item">Irish $7.95</div>
    <div class="desc">Skillet full of hash browns, onions, peppers &amp; mushrooms topped with cheese and 2 eggs.&nbsp; Served w/ Toast.</div>
    <div class="item">Melting Pot $8.95</div>
    <div class="desc">Skillet full of hash browns, ham, bacon, sausage, mushrooms, onions, tomatoes and peppers topped with cheese and 2 eggs.<br>Served with toast.</div>
    <div class="item feature">Biscuits &amp; Gravy $7.95</div>
    <div class="desc feature">Skillet full of hash browns, onions, peppers &amp; cheese.&nbsp; Topped w/ homemade biscuit, sausage gravy &amp; 2 eggs.</div>
  </section>

  <section class="section" style="left:70px;top:239px">
    <h2>Omelettes</h2>
    <div class="desc">Fluffy Pan-Fried Omelettes, Served w/ Hash Browns &amp; Toast</div>
    <div class="item">Athenian $8.95</div>
    <div class="desc">Gyro off-the-cone, tomatoes, onions, olives, &amp; feta cheese.&nbsp; Served with side of homemade cucumber sauce.</div>
    <div class="item">Denver $7.95</div>
    <div class="desc">Ham, onion, pepper &amp; cheese.</div>
    <div class="item">Veggie $7.95</div>
    <div class="desc">Onions, peppers, tomatoes &amp; mushrooms</div>
    <div class="item">Deluxe $8.95</div>
    <div class="desc">Ham, bacon, sausage, mushrooms, onions, tomatoes and peppers.</div>
    <div class="item feature">Spinach Pesto $8.95</div>
    <div class="desc feature">Sun-Dried tomatoes, spinach, mushrooms &amp; cheese. Topped w/ Pesto Cream Sauce</div>
    <div class="item">Ham &amp; Cheese $6.95</div>
  </section>

  <section class="section" style="left:70px;top:423px">
    <h2>Pancakes, French Toast &amp; Waffles</h2>
    <div class="item">Apple Danish French Toast $6.95</div>
    <div class="item">Bananas Foster Pancakes $7.95</div>
    <div class="item">Strawberry Cake Waffle $7.95</div>
    <div class="item">Pancakes or French Toast (2) $4.55 / (3) $4.95</div>
    <div class="item">Belgium Waffle $4.95</div>
    <div class="item">Add Fruit Topping, Bacon, Ham or Sausage $1.95</div>
  </section>

  <section class="section" style="left:341px;top:423px">
    <h2>Light Breakfast</h2>
    <div class="item">Egg, Sausage, &amp; Cheese Sand. $4.25</div>
    <div class="item">Oatmeal or Cereal $3.55&nbsp; w/ raisins $3.95</div>
    <div class="item">Bagel w/ cream cheese $2.55</div>
    <div class="item">English Muffin or Raisin Toast $1.55</div>
    <div class="item">Fresh Fruit Bowl $4.95</div>
    <div class="item feature">Mediterranean Pita $6.95</div>
    <div class="desc feature">Pesto Spread on Pita Bread w/ spinach, tomatoes,<br>feta &amp; an Egg.</div>
  </section>

  <section class="section" style="left:70px;top:553px">
    <h2>Eggs &amp; Specialties</h2>
    <div class="item">Two Eggs, Hash Browns &amp; Toast $4.95</div>
    <div class="item indent">With Bacon, Sausage or Ham $5.95</div>
    <div class="item indent">With Corned Beef Hash $6.55</div>
    <div class="item indent">With Gyro off-the-cone $6.95</div>
    <div class="item">Steak &amp; Eggs $13.95</div>
    <div class="desc">8oz Prime Cut Steak, 2 Eggs, hash browns, &amp; Toast.</div>
    <div class="item">Chop Steak &amp; Eggs $9.95</div>
    <div class="desc">10oz Chopped Sirloin Steak, 2 Eggs, hash browns, &amp; Toast.</div>
    <div class="item">Granny’s Breakfast $6.95</div>
    <div class="desc">Two Eggs scrambled w/ potatoes, ham, onions &amp; peppers topped w/ cheese.&nbsp; Served with toast.</div>
    <div class="item">3 Deuces $6.95</div>
    <div class="desc">Two Eggs, Two Pancakes &amp; Two Sausage Links or Bacon Strips.</div>
    <div class="item">Homemade Biscuits &amp; Gravy&nbsp; Half $3.95&nbsp; /&nbsp; Full $5.55</div>
  </section>

  <div class="page-divider"></div>

  <div class="cover-stripe"></div>
  <section class="cover">
    <h1 class="cover-title">MENU</h1>
    <div class="brand">
      <span class="brand-dot"></span>
      <span class="brand-name">58 Restaurant &amp; Bar</span>
    </div>
    <div class="contact">
      <p>58 N Harbor St · Lakeview, WI 53900</p>
      <p>262-555-0158</p>
      <p>www.58restaurant.com</p>
    </div>
    <p class="cover-note">Serving Breakfast Saturday &amp; Sunday</p>
    <div class="cover-extras">
      <p>Catering &amp; Private Party Hosting Available</p>
      <p>Friday Fish Fry · Saturday Prime Rib</p>
    </div>
  </section>
</div>
</body>
</html>
```